U.S. Popcorn company needs business cards

We are a popcorn company that manufactures popcorn and sells it to grocery stores worldwide. Our theme is "Americana" and our logo is U.S. route 66 which is the most famous highway in the U.S.

We would like the design to be simple and to use both sides. On the back side we would like to see just the logo and website. The front would be normal details

Target Market(s)

Wholesalers, grocers and distributors

Industry/Entity Type

Manufacture

Contact Information for Business Card

Business name: Bluebell Ridge Popcorn
Phone: +1 555 014 2286
Email: Derek@bluebellridgepopcorn.com
website: www.bluebellridgepopcorn.com
Tag Line: "POPular for a reason"
Name: Derek Halvorsen
Title: Founder/President

Requirements
Must have
• Either this design should be fun or clean and simple. I will let you show me your thougths.
Nice to have
• Anything that ties in the real Hwy Route 66.
• Colors might need to be red, white and blue incorporated.
Should not have
• Not be too busy.

```html
<!DOCTYPE html>
<html lang="en">
<head>
<meta charset="utf-8">
<title>Bluebell Ridge Popcorn – Business Cards</title>
<link rel="stylesheet" href="https://fonts.googleapis.com/css2?family=Lato:wght@400;700;900&family=Raleway:wght@700&display=swap">
<style>
  :root {
    --stage: #ececec;
    --card: #ffffff;
    --red: #e31e26;
    --navy: #0f2a6b;
    --ink: #1c1c1c;
    --photo-light: #f1ece8;
    --photo-mid: #e6dcd3;
  }
  * { margin: 0; padding: 0; box-sizing: border-box; }
  html, body { width: 1200px; height: 586px; overflow: hidden; }
  body {
    background: var(--stage);
    position: relative;
    font-family: "Lato", sans-serif;
  }
  .card {
    position: absolute;
    top: 129px;
    width: 502px;
    height: 301px;
    background: var(--card);
    overflow: hidden;
  }
  .card--back { left: 61px; }
  .card--front { left: 619px; }

  .back-photo {
    position: absolute; inset: 0;
    background: radial-gradient(ellipse at 50% 45%, var(--photo-light) 0%, var(--photo-mid) 100%);
  }

  .holder { position: absolute; left: 36px; top: 49px; }
  .holder__name {
    font-family: "Raleway", sans-serif;
    font-weight: 700;
    font-size: 16px;
    color: var(--red);
    line-height: 1;
  }
  .holder__title {
    margin-top: 6px;
    font-size: 11px;
    color: var(--ink);
  }

  .contact-tab {
    position: absolute;
    left: 0; top: 161px;
    width: 42px; height: 101px;
    background: var(--red);
    border-radius: 0 10px 10px 0;
  }
  .contact-tab svg { position: absolute; left: 13px; width: 16px; height: 16px; }

  .contact-list { position: absolute; left: 54px; top: 174px; list-style: none; }
  .contact-list li {
    font-size: 12.5px;
    font-weight: 700;
    color: var(--ink);
    height: 30px;
    line-height: 16px;
    letter-spacing: 0.2px;
  }

  .brand {
    position: absolute;
    left: 275px; top: 80px;
    width: 200px; height: 150px;
    display: flex; flex-direction: column; align-items: center; justify-content: center;
    gap: 10px;
  }
  .brand__dot { width: 22px; height: 22px; border-radius: 50%; background: var(--red); }
  .brand__name {
    font-family: "Lato", sans-serif;
    font-weight: 900;
    font-size: 22px;
    line-height: 1.15;
    color: var(--navy);
    text-align: center;
    text-transform: uppercase;
  }

  .band { position: absolute; bottom: 0; }
  .band--navy { left: 0; width: 310px; height: 11px; background: var(--navy); }
  .band--red {
    left: 301px; right: 0; height: 14px;
    background: var(--red);
    border-top-left-radius: 14px;
    box-shadow: -3px 0 0 var(--card);
  }
</style>
</head>
<body>
  <section class="card card--back">
    <div class="back-photo" role="img" aria-label="Photo of a red and white striped popcorn box filled with popcorn on a white plate, brand label on the box"></div>
  </section>

  <section class="card card--front">
    <div class="holder">
      <p class="holder__name">Derek Halvorsen</p>
      <p class="holder__title">Founder/President</p>
    </div>

    <div class="contact-tab">
      <svg style="top:14px" viewBox="0 0 24 24" aria-hidden="true"><path fill="#fff" d="M6.6 10.8a15 15 0 0 0 6.6 6.6l2.2-2.2a1 1 0 0 1 1-.25 11.4 11.4 0 0 0 3.6.57 1 1 0 0 1 1 1V20a1 1 0 0 1-1 1A17 17 0 0 1 3 4a1 1 0 0 1 1-1h3.5a1 1 0 0 1 1 1c0 1.25.2 2.45.57 3.57a1 1 0 0 1-.25 1z"/></svg>
      <svg style="top:43px" viewBox="0 0 24 24" aria-hidden="true"><rect x="2" y="5" width="20" height="14" rx="1.5" fill="none" stroke="#fff" stroke-width="2"/><path d="M2.5 6l9.5 7 9.5-7" fill="none" stroke="#fff" stroke-width="2"/></svg>
      <svg style="top:73px" viewBox="0 0 24 24" aria-hidden="true"><path d="M10 14a4 4 0 0 0 5.7 0l3.6-3.6a4 4 0 0 0-5.7-5.7l-1.3 1.3M14 10a4 4 0 0 0-5.7 0l-3.6 3.6a4 4 0 0 0 5.7 5.7l1.3-1.3" fill="none" stroke="#fff" stroke-width="2.2" stroke-linecap="round"/></svg>
    </div>

    <ul class="contact-list">
      <li>+1 555 014 2286</li>
      <li>Derek@bluebellridgepopcorn.com</li>
      <li>www.bluebellridgepopcorn.com</li>
    </ul>

    <div class="brand">
      <span class="brand__dot"></span>
      <p class="brand__name">Bluebell Ridge<br>Popcorn</p>
    </div>

    <div class="band band--navy"></div>
    <div class="band band--red"></div>
  </section>
</body>
</html>
```